Web Design Project for an IT product called "TAVEXO"

Hello!

We need a web design for a new IT product called "TAVEXO". The product consists of 2 software applications, one is on an Android based tablet, the other on a windows 7 computer. The system is used in the production for conducting time studies (e.g. everything that has to do with time measuring in the production). The design should include the company logo ("DRUL"), and the logo of the methodology used ("VOMI" - see www.vomi-example.de), the rest is up to you! We already made a concept for the app logo, but it can be tweaked in any way...
Updates

Will upload a document with exact description!

Updated the files... Made some screenshots of the app on the Android device & Windows 7

Reason: Will make a poll & let you know the decision tomorrow!

Target Market(s)

Larger production companies middle management, technology departments

Industry/Entity Type

Computer

Requirements
Must have
• - company logo "DRUL" - included
- methodology logo "VOMI" (see www.vomi-example.de) - included
Nice to have
• - our logo of the app tweaked and somehow integrated

```html
<!DOCTYPE html>
<html lang="en">
<head>
<meta charset="utf-8">
<title>TAVEXO 3.0 – Work and Time Study</title>
<link rel="stylesheet" href="https://fonts.googleapis.com/css2?family=Quicksand:wght@300;400&family=Arimo:wght@400;700&display=swap">
<style>
  :root {
    --band-blue: #1f8bc4;
    --circle-blue: #145e8f;
    --button-blue: #1878b2;
    --band-text: #dcedf8;
    --white: #ffffff;
    --heading-dark: #2f2f2f;
    --body-grey: #555555;
    --note-bg: #f4eab6;
    --note-label: #e5cf66;
    --note-label-text: #7a6420;
    --note-text: #b8892a;
    --link-blue: #2a86c6;
    --rule: #cfcfcf;
  }
  * { box-sizing: border-box; margin: 0; padding: 0; }
  html, body { width: 1200px; height: 900px; overflow: hidden; background: var(--white); }
  body { font-family: "Arimo", Arial, sans-serif; color: var(--body-grey); position: relative; }

  .feature-band { position: absolute; left: 0; top: 0; width: 1200px; height: 375px; background: var(--band-blue); }
  .feature { position: absolute; top: 38px; width: 270px; text-align: center; color: var(--band-text); }
  .feature--mobile { left: 161px; }
  .feature--advantages { left: 465px; }
  .feature--concepts { left: 769px; }
  .feature__icon { width: 76px; height: 76px; border-radius: 50%; background: var(--circle-blue); margin: 0 auto; display: flex; align-items: center; justify-content: center; }
  .feature__title { font-family: "Quicksand", sans-serif; font-weight: 300; font-size: 24px; line-height: 39px; color: var(--white); margin-top: 11px; letter-spacing: 0.5px; width: 300px; margin-left: -15px; }
  .feature__text { font-size: 14px; line-height: 21.5px; margin-top: 7px; padding: 0 14px; }
  .feature__text strong { color: var(--white); }
  .feature__button { display: inline-block; margin-top: 10px; background: var(--button-blue); color: var(--band-text); font-size: 13px; line-height: 22px; padding: 0 10px; border-radius: 3px; text-decoration: none; }

  .content { position: absolute; left: 201px; top: 424px; width: 495px; }
  .content h2 { font-size: 17px; line-height: 20px; color: var(--heading-dark); font-weight: 700; }
  .content p { font-size: 12px; line-height: 19.5px; margin-top: 10px; }
  .content p strong { color: var(--heading-dark); }

  .note { margin-top: 10px; background: var(--note-bg); height: 94px; position: relative; }
  .note__label { position: absolute; left: 0; top: 0; width: 63px; height: 22px; background: var(--note-label); color: var(--note-label-text); font-size: 11px; font-weight: 700; line-height: 22px; text-align: center; }
  .note__text { position: absolute; left: 33px; top: 34px; right: 20px; font-size: 12px; line-height: 19.5px; color: var(--note-text); }
  .note__text a { color: #7a5a10; text-decoration: none; }

  .divider { margin-top: 28px; border-top: 2px dotted var(--rule); }

  .advantages h2 { margin-top: 35px; font-size: 18px; }
  .advantages__lists { display: flex; margin-top: 8px; }
  .advantages ul { list-style: none; font-size: 12px; line-height: 20px; width: 258px; }
  .advantages ul + ul { width: 237px; }
  .advantages li::before { content: "\2794"; font-size: 10px; color: var(--heading-dark); margin-right: 5px; }
  .advantages__more { display: inline-block; margin-top: 8px; font-size: 12px; color: var(--link-blue); text-decoration: none; }

  .product-visual { position: absolute; left: 736px; top: 428px; width: 340px; height: 432px; background: linear-gradient(160deg, #1b1d22 0%, #2a2f38 45%, #f2f2f2 60%, #ffffff 100%); border-radius: 14px; }
</style>
</head>
<body>
  <section class="feature-band">
    <article class="feature feature--mobile">
      <div class="feature__icon">
        <svg width="30" height="30" viewBox="0 0 30 30" fill="#fff"><path d="M17 2h11v11l-4-4-5 5-3-3 5-5zM13 28H2V17l4 4 5-5 3 3-5 5z"/></svg>
      </div>
      <h3 class="feature__title">A Mobile and Stationary Application</h3>
      <p class="feature__text">In the year 2005 DRUL d.o.o. successfully develeoped and launched a product called <strong>TAVEXO 2.0</strong>. Its purpose...</p>
      <a class="feature__button" href="#">Read more »</a>
    </article>
    <article class="feature feature--advantages">
      <div class="feature__icon">
        <svg width="24" height="30" viewBox="0 0 24 30" fill="#fff"><path d="M1 0h22v30l-11-9-11 9z"/></svg>
      </div>
      <h3 class="feature__title">Advantages of the System</h3>
      <p class="feature__text">An extremely competitive price compared to the other systems. Fast and easy time data gathering - no paper!</p>
      <a class="feature__button" href="#">Read more »</a>
    </article>
    <article class="feature feature--concepts">
      <div class="feature__icon">
        <svg width="34" height="28" viewBox="0 0 34 28" fill="none" stroke="#fff" stroke-width="2.4"><rect x="1.5" y="1.5" width="31" height="25"/><path d="M1.5 9h31M1.5 15h31M1.5 21h31M9 9v17.5M17 9v17.5M25 9v17.5"/></svg>
      </div>
      <h3 class="feature__title">TAVEXO 3.0 Concepts and Requirements</h3>
      <p class="feature__text"><strong>TAVEXO 3.0</strong> still consists of 2 applications: the first one is running on a PC, and a second one that is running on the tablet.</p>
      <a class="feature__button" href="#">Read more »</a>
    </article>
  </section>

  <main class="content">
    <h2>A mobile and stationary application TAVEXO 3.0<br>for the needs of work and time study.</h2>
    <p>The goal was to develop an application that runs on <strong>Corvin OS</strong> or PDAs. TAVEXO became the first slovenian application , that was based strictly on VOMI standards; it was ment for technologists, analysts and everybody that need to gather and process time data in the production.</p>
    <div class="note">
      <span class="note__label">NOTE</span>
      <p class="note__text">The system was very successful on the slovenian market; nowadays more than 50 companies are using it plus both machine faculties. <a href="#">Learn more »</a></p>
    </div>
    <div class="divider"></div>
    <section class="advantages">
      <h2>Advantages of the system TAVEXO 3.0:</h2>
      <div class="advantages__lists">
        <ul>
          <li>An extremely competitive price</li>
          <li>Fast and easy time data gathering</li>
          <li>Multitask use in the field of time and work study</li>
          <li>Possibility of upgradin the system</li>
        </ul>
        <ul>
          <li>The evaluation of the recording is done automatically</li>
          <li>Automatical statistical analysis</li>
          <li>WiFi support for data transfer</li>
          <li>Photo / video documentation possibilites</li>
        </ul>
      </div>
      <a class="advantages__more" href="#">Read all advantages »</a>
    </section>
  </main>

  <div class="product-visual" role="img" aria-label="Tablet showing the TAVEXO app with the app logo card in front"></div>
</body>
</html>
```